Business Card Design Project

Looking for a logo and business card for a Real State Business i will be opening. The name is not choosen yet , but will probably be RTV IMOVEIS.
I was thinking black and silver colors, but am open to nice ideas.
I did add a business card that i liked a lot, am looking for something like that, with logo in black or silver in a black card. The logo i was thinking in the letters RTV as i uploaded or something or little and cute buildings or a house...just ideas, can be any nice logo.
Updates

You guys can add other colors if you want, I like colors very "BRIGHT" and "open", like red, pink, strong colors. almost glow in the dark colors. lol

Designers,

I've increased more 88 dollars in the budget for 1st place cause I will want envelope designs... small and big sizes.

So 1st place is now U$248,00. 

No need to send the envelope designs right now... only the business cards designs.

Thank you.

Industry/Entity Type

Business

Requirements
Must have
• Renata Tavares Vilela

www.RTVimoveis-exemplo.com.br

+554188316402

renata@rtvimoveis-exemplo.com.br

```html
<!DOCTYPE html>
<html lang="pt-BR">
<head>
<meta charset="UTF-8">
<title>RTV IMOVEIS – Cartão de visita</title>
<link rel="stylesheet" href="https://fonts.googleapis.com/css2?family=Jost:wght@300&display=swap">
<style>
  :root {
    --backdrop: #e9e6e1;
    --card: #030303;
    --ink: #ffffff;
    --ink-soft: #d6d6d6;
    --silver: #f4f4f4;
    --silver-mid: #8f8f8f;
    --rule: #9a9a9a;
  }
  * { margin: 0; padding: 0; box-sizing: border-box; }
  html, body {
    width: 1200px; height: 900px; overflow: hidden;
    background: var(--backdrop);
    font-family: "Jost", sans-serif;
  }
  .canvas { position: relative; width: 1200px; height: 900px; }

  .card {
    position: absolute;
    width: 600px; height: 340px;
    background: var(--card);
    overflow: hidden;
    box-shadow: 0 10px 28px rgba(0,0,0,.35);
  }
  .card--front { left: 140px; top: 60px; }
  .card--back  { left: 460px; top: 490px; }

  .brand-name {
    position: absolute;
    color: var(--ink);
    font-family: "Jost", sans-serif;
    font-weight: 300;
    letter-spacing: 4px;
    white-space: nowrap;
  }
  .card--front .brand-name { left: 50px; top: 70px; font-size: 26px; }
  .card--back .brand-name {
    left: 50%; top: 50%;
    transform: translate(-50%, -50%);
    font-size: 42px; letter-spacing: 6px;
  }

  .rule {
    position: absolute; height: 1px;
    background: linear-gradient(90deg, transparent, var(--rule) 15%, var(--rule) 85%, transparent);
  }
  .rule--top { left: 80px; right: 20px; top: 112px; }
  .rule--mid { left: 0; right: 20px; top: 160px; }
  .rule--band { left: 0; right: 20px; top: 211px; }
  .rule--bottom { left: 40px; right: 20px; top: 272px; }

  .silver-band {
    position: absolute; left: 0; top: 161px; width: 330px; height: 50px;
    background: linear-gradient(90deg, var(--silver) 0%, var(--silver) 12%, var(--silver-mid) 45%, #2a2a2a 75%, var(--card) 100%);
  }

  .holder-name {
    position: absolute; right: 40px; top: 125px;
    color: var(--ink-soft);
    font-weight: 300; font-size: 18px; letter-spacing: .3px;
  }

  .contacts {
    position: absolute; left: 40px; right: 20px; top: 290px;
    display: flex; justify-content: space-between; align-items: center;
    list-style: none;
    color: var(--ink-soft);
    font-weight: 300; font-size: 11.5px;
  }
  .contacts li { display: flex; align-items: center; gap: 6px; white-space: nowrap; }
  .contacts svg { width: 12px; height: 12px; fill: none; stroke: var(--ink); stroke-width: 1.6; }
</style>
</head>
<body>
<main class="canvas">

  <section class="card card--front" aria-label="Frente do cartão">
    <p class="brand-name">RTV IMOVEIS</p>
    <div class="rule rule--top"></div>
    <p class="holder-name">Renata Tavares Vilela</p>
    <div class="rule rule--mid"></div>
    <div class="silver-band"></div>
    <div class="rule rule--band"></div>
    <div class="rule rule--bottom"></div>
    <ul class="contacts">
      <li>
        <svg viewBox="0 0 12 12"><rect x="3.2" y="1" width="5.6" height="10" rx="1"/><line x1="5" y1="9.2" x2="7" y2="9.2"/></svg>
        554 188 316 402
      </li>
      <li>
        <svg viewBox="0 0 12 12"><rect x="1" y="2.5" width="10" height="7"/><polyline points="1,2.5 6,6.8 11,2.5"/></svg>
        renata@rtvimoveis-exemplo.com.br
      </li>
      <li>
        <svg viewBox="0 0 12 12"><circle cx="6" cy="6" r="5"/><ellipse cx="6" cy="6" rx="2.2" ry="5"/><line x1="1" y1="6" x2="11" y2="6"/></svg>
        www.RTVimoveis-exemplo.com.br
      </li>
    </ul>
  </section>

  <section class="card card--back" aria-label="Verso do cartão">
    <p class="brand-name">RTV IMOVEIS</p>
  </section>

</main>
</body>
</html>
```